hop3PeakTrail

I have a weebly web site need design and formatted using the color and look and feel similar to another site. Our web site is currently behind password. http://www.hop3peaktrail.com pwd Blue7RiverLamp!

I'm looking to layout like https://www.kravlinpartners.com/blog

We want a yellow, light yellow, gray and black as the main colors. Attached image show color of yellow and light yellow. I don't have a specific color for gray and black. If you think there should be addition colors in the color pallet we greatly appreciate your expertise.

We need the logo designed. Right now its just text.

I don't like that our site list the full blog one after another, I like the tiled look, image, tile and small amount of text. Click and go into a blog. Often at the end of a blog you can jump back to main page, and/or see three additional blog tiles. We like how orange carries through on buttons and text, Accent colors are consistent.

I need CSS that can be inserted into each form. If you look at the source of the form, you can see how I tried to format given the form elements. I cannot change the form, but I can easily insert CSS for the form.

I need a template that can be used in Weebly site either you edit on our site or give us a template that can be used.

Industry/Entity Type

Life Coaching

Coding

Coded - Design and coding required

Number of Pages Required

5+ page

Font styles to use
Sans Serif

Requirements
Must have
• What to build a clean color pallet using the Yellow, light yellow I uploaded image. Also a gray and black.

```html
<!DOCTYPE html>
<html lang="en">
<head>
<meta charset="utf-8">
<title>hop3PeakTrail – Blog</title>
<link href="https://fonts.googleapis.com/css2?family=Oswald:wght@600&family=Roboto:wght@500;700;900&family=IBM+Plex+Sans:wght@400;500&display=swap" rel="stylesheet">
<style>
:root{
  --yellow:#fcbf0b;
  --yellow-soft:#fde48c;
  --yellow-pale:#fff3cf;
  --ink:#0d0d0d;
  --gray-bg:#f1f1f1;
  --gray-text:#3a3a3a;
  --gray-meta:#8a8a8a;
  --line:#d9d9d9;
  --navy:#0e1722;
  --white:#ffffff;
}
*{box-sizing:border-box;margin:0;padding:0}
html,body{width:1200px;height:2992px;overflow:hidden}
body{position:relative;font-family:"IBM Plex Sans",Arial,sans-serif;color:var(--ink);background:var(--gray-bg)}
.abs{position:absolute}

/* Hero */
.hero{left:0;top:0;width:1200px;height:561px;background:linear-gradient(180deg,#7fb3ae 0%,#b9c0a3 30%,#e7b77c 60%,#d9803a 85%,#b9571f 100%)}
.hero-glow{left:600px;top:90px;width:520px;height:460px;background:radial-gradient(circle at 50% 40%,rgba(255,240,210,.85),rgba(255,220,170,0) 60%)}
.hero-hands{left:610px;top:340px;width:590px;height:221px;background:linear-gradient(160deg,rgba(60,25,10,0) 0%,rgba(60,25,10,.55) 60%,rgba(40,15,5,.8) 100%)}
.logo{font-family:Roboto,Arial,sans-serif;font-weight:700;font-size:31px;color:var(--white);letter-spacing:.2px}
.header-logo{left:99px;top:13px}
.nav{top:25px;display:flex;gap:0;font-family:Roboto,Arial,sans-serif;font-weight:500;font-size:14px;text-transform:uppercase}
.nav a{position:absolute;color:var(--ink);text-decoration:none;white-space:nowrap}
.btn{display:flex;align-items:center;justify-content:center;background:var(--yellow);color:var(--white);font-family:Roboto,Arial,sans-serif;font-weight:700;text-transform:uppercase}
.header-cta{left:940px;top:14px;width:159px;height:39px;font-size:15px}
.hero-title{left:98px;top:192px;font-family:Oswald,Impact,sans-serif;font-weight:600;font-size:60px;line-height:70px;letter-spacing:.5px}
.hero-text{left:100px;top:265px;width:500px;font-size:14.5px;line-height:24px;color:#1c1c1c}
.hero-form{left:100px;top:332px;width:478px;height:48px;background:var(--white);display:flex;align-items:center}
.hero-form span{padding-left:12px;font-size:14px;color:#8d8d8d;flex:1}
.hero-form .btn{width:144px;height:42px;margin-right:3px;font-size:15px}

/* Blog section */
.blog{left:0;top:561px;width:1200px;height:1530px;background:linear-gradient(135deg,#f7f7f7 0%,#ececec 40%,#f5f5f5 70%,#eeeeee 100%)}
.badge{left:472px;top:677px;width:237px;height:48px;font-size:28px;font-weight:700}
.section-title{left:0;width:1200px;top:736px;text-align:center;font-family:Roboto,Arial,sans-serif;font-weight:900;font-size:46px}
.filters{left:98px;top:823px;font-family:Roboto,Arial,sans-serif;font-weight:700;font-size:14.5px}
.filters span{position:absolute;white-space:nowrap}
.filters .active{color:var(--yellow);font-weight:500}
.search{left:710px;top:811px;width:389px;height:46px;background:var(--white);border:1px solid var(--line);display:flex;align-items:center}
.search span{flex:1;padding-left:19px;font-size:14px;color:#7a7a7a}
.search .icon{width:42px;height:40px;margin-right:2px;background:var(--yellow);display:flex;align-items:center;justify-content:center}

.card{position:absolute;width:320px;height:523px}
.card-photo{position:absolute;left:0;top:0;width:320px;height:235px}
.card-body{position:absolute;left:13px;top:235px;width:294px;height:288px;background:var(--white);box-shadow:0 4px 14px rgba(0,0,0,.08);overflow:hidden}
.card-title{position:absolute;left:13px;top:187px;width:294px;height:48px;background:var(--yellow);color:var(--white);font-family:Roboto,Arial,sans-serif;font-weight:700;font-size:19px;line-height:48px;padding-left:15px;text-transform:uppercase;white-space:nowrap}
.card-meta{position:absolute;left:16px;top:14px;font-size:10.5px;color:var(--gray-meta);display:flex;gap:14px}
.card-meta i{display:inline-block;width:11px;height:11px;border-radius:50%;background:#c9c9c9;vertical-align:-1px;margin-right:4px}
.card-meta b{display:inline-block;width:11px;height:10px;background:#c9c9c9;vertical-align:-1px;margin-right:4px;font-weight:400}
.card-text{position:absolute;left:16px;top:40px;width:272px;font-size:15px;line-height:24px;color:var(--gray-text)}
.card-link{position:absolute;left:15px;top:199px;font-family:Roboto,Arial,sans-serif;font-weight:700;font-size:15px;color:var(--yellow)}
.card-wave{position:absolute;left:0;bottom:0;width:294px;height:90px}

.pager{left:511px;top:2022px;display:flex;gap:5px}
.pager span{width:32px;height:32px;border:1px solid var(--line);background:var(--white);display:flex;align-items:center;justify-content:center;font-family:Roboto,Arial,sans-serif;font-size:17px}
.pager .current{background:var(--yellow);border-color:var(--yellow)}

/* About */
.about{left:0;top:2091px;width:1200px;height:560px;background:linear-gradient(180deg,#f1f2f4 0%,#d8dde4 35%,#aab4c2 70%,#6d7a8c 100%)}
.about-peak{left:860px;top:2260px;width:340px;height:380px;background:linear-gradient(180deg,rgba(30,30,35,0) 0%,rgba(30,30,35,.45) 55%,rgba(25,25,30,.9) 100%)}
.about-title{left:105px;top:2152px;font-family:Roboto,Arial,sans-serif;font-weight:900;font-size:46px}
.about-text{left:105px;top:2223px;width:476px;font-size:18px;line-height:31.4px;text-align:justify;color:#1c1c1c}
.about-btn{left:106px;top:2415px;width:194px;height:44px;font-size:17px}

/* Footer */
.footer-wave{left:0;top:2540px;width:1200px;height:100px}
.footer{left:0;top:2630px;width:1200px;height:362px;background:var(--navy);color:var(--white)}
.footer-logo{left:103px;top:2704px;font-size:34px}
.social{top:2778px;width:33px;height:33px;border-radius:50%;background:var(--white)}
.footer-col{top:2705px;font-family:Roboto,Arial,sans-serif}
.footer-col h4{font-weight:700;font-size:17px;margin-bottom:9px;text-transform:uppercase}
.footer-col a{display:block;color:var(--white);font-family:"IBM Plex Sans",Arial,sans-serif;font-size:15.5px;line-height:31.3px;text-decoration:none}
.news-text{font-family:"IBM Plex Sans",Arial,sans-serif;font-weight:500;font-size:13px;line-height:21px;margin-bottom:14px;width:220px}
.news-input{width:232px;height:41px;background:var(--white);color:#777;font-family:"IBM Plex Sans",Arial,sans-serif;font-size:12px;padding:13px 11px}
.news-btn{width:115px;height:39px;margin-top:9px;font-size:16px;font-weight:500}
.footer-rule{left:100px;top:2924px;width:999px;height:1px;background:#4b525b}
.copyright{left:0;width:1200px;top:2943px;text-align:center;font-size:15.5px}
</style>
</head>
<body>

<section class="abs hero" role="img" aria-label="Sunset sky with hands reaching up to a glowing network globe"></section>
<div class="abs hero-glow" role="img" aria-label="Glowing connected network globe"></div>
<div class="abs hero-hands" role="img" aria-label="Silhouetted hands holding the globe"></div>

<header>
  <div class="abs logo header-logo">hop3PeakTrail</div>
  <nav class="abs nav">
    <a style="left:381px">Blog</a>
    <a style="left:447px">Who We Are</a>
    <a style="left:560px">Our Model</a>
    <a style="left:667px">Who Uses hop3PeakTrail</a>
    <a style="left:862px">Pricing</a>
  </nav>
  <div class="abs btn header-cta">Subscribe Now</div>
</header>

<h1 class="abs hero-title">FINDING JOY IN CHAOS</h1>
<p class="abs hero-text">Lorem ipsum dolor sit amet, consecteturpiscing elit, seo eiusmod tempor incididunt ut labore et dolore magna aliqua.</p>
<div class="abs hero-form"><span>Subscribe to the Blog</span><div class="btn">Subscribe Now</div></div>

<section class="abs blog"></section>
<div class="abs btn badge">LATEST BLOG</div>
<h2 class="abs section-title">FOR OUR CLIENTS</h2>
<div class="abs filters">
  <span class="active" style="left:0">All</span>
  <span style="left:42px">|</span>
  <span style="left:73px">Career</span>
  <span style="left:141px">|</span>
  <span style="left:171px">Finance</span>
  <span style="left:248px">|</span>
  <span style="left:278px">Health</span>
  <span style="left:346px">|</span>
  <span style="left:376px">Tool</span>
</div>
<div class="abs search"><span>Search the Blog....</span>
  <div class="icon"><svg width="24" height="24" viewBox="0 0 24 24" fill="none" stroke="#111" stroke-width="1.8"><circle cx="11" cy="11" r="8"/><path d="M17 17l5 5"/></svg></div>
</div>

<!-- Row 1 -->
<article class="card" style="left:100px;top:886px">
  <div class="card-photo" role="img" aria-label="Team meeting around a table under a hanging bulb" style="background:linear-gradient(160deg,#dfe3e6,#7d8a92 60%,#3d3a36)"></div>
  <div class="card-title">Improvisation</div>
  <div class="card-body">
    <div class="card-meta"><span><i></i>Coach Rae</span><span><b></b>16 December 2020</span></div>
    <p class="card-text">Essential to living a joyful life is the ability to adapt to any situation. Life is always going to throw curveballs, and we’re always going to need to find a different way to respond to a new play. We need to improvise.</p>
    <span class="card-link">LEARN MORE</span>
    <svg class="card-wave" viewBox="0 0 294 90" preserveAspectRatio="none"><path d="M0 50 C60 40 90 80 150 50 C200 25 240 20 294 35 V90 H0Z" fill="var(--yellow-pale)"/><path d="M0 58 C60 48 90 88 150 58 C200 33 240 28 294 43 V90 H0Z" fill="var(--yellow-soft)"/></svg>
  </div>
</article>
<article class="card" style="left:439px;top:886px">
  <div class="card-photo" role="img" aria-label="Group of hands joined together in a circle" style="background:linear-gradient(150deg,#4a4f52,#8a8a7e 55%,#b28a45)"></div>
  <div class="card-title">Strong Values</div>
  <div class="card-body">
    <div class="card-meta"><span><i></i>Coach Rae</span><span><b></b>16 December 2020</span></div>
    <p class="card-text">We are protected by our values and our core beliefs. They are a vital aspect in resilience. The importance of values can be seen from religion to the most successful companies. Likely, we all have at least someone</p>
    <span class="card-link">LEARN MORE</span>
    <svg class="card-wave" viewBox="0 0 294 90" preserveAspectRatio="none"><path d="M0 50 C60 40 90 80 150 50 C200 25 240 20 294 35 V90 H0Z" fill="var(--yellow-pale)"/><path d="M0 58 C60 48 90 88 150 58 C200 33 240 28 294 43 V90 H0Z" fill="var(--yellow-soft)"/></svg>
  </div>
</article>
<article class="card" style="left:777px;top:886px">
  <div class="card-photo" role="img" aria-label="Woman with open arms overlooking a city skyline" style="background:linear-gradient(180deg,#caa06a,#6b5a48 50%,#3a322c)"></div>
  <div class="card-title">Realistic Optimism</div>
  <div class="card-body">
    <div class="card-meta"><span><i></i>Coach Rae</span><span><b></b>16 December 2020</span></div>
    <p class="card-text">The best outlook in life is to approach it with realistic optimism. That might sound like an oxymoron, but is in fact key to living a resilient life. It is true that looking at life through rose colored glasse</p>
    <span class="card-link">LEARN MORE</span>
    <svg class="card-wave" viewBox="0 0 294 90" preserveAspectRatio="none"><path d="M0 50 C60 40 90 80 150 50 C200 25 240 20 294 35 V90 H0Z" fill="var(--yellow-pale)"/><path d="M0 58 C60 48 90 88 150 58 C200 33 240 28 294 43 V90 H0Z" fill="var(--yellow-soft)"/></svg>
  </div>
</article>

<!-- Row 2 -->
<article class="card" style="left:100px;top:1451px">
  <div class="card-photo" role="img" aria-label="Smiling woman checking her phone in a bright hallway" style="background:linear-gradient(120deg,#f3e2d6,#d9c3bb 50%,#9e8b86)"></div>
  <div class="card-title">Let’s Talk Net Worth</div>
  <div class="card-body">
    <div class="card-meta"><span><i></i>Coach Rae</span><span><b></b>16 December 2020</span></div>
    <p class="card-text">You should be tracking your net worth. Your net worth is a very helpful number in tracking your finances and helping you focus on reducing debt and increasing the value of your assets.</p>
    <span class="card-link">LEARN MORE</span>
    <svg class="card-wave" viewBox="0 0 294 90" preserveAspectRatio="none"><path d="M0 50 C60 40 90 80 150 50 C200 25 240 20 294 35 V90 H0Z" fill="var(--yellow-pale)"/><path d="M0 58 C60 48 90 88 150 58 C200 33 240 28 294 43 V90 H0Z" fill="var(--yellow-soft)"/></svg>
  </div>
</article>
<article class="card" style="left:439px;top:1451px">
  <div class="card-photo" role="img" aria-label="Hiker resting on a rocky mountain summit under blue sky" style="background:linear-gradient(180deg,#3d72c4,#86a9d6 45%,#7a6f64 75%,#4c463f)"></div>
  <div class="card-title">Climbing a Mountain</div>
  <div class="card-body">
    <div class="card-meta"><span><i></i>Coach Rae</span><span><b></b>16 December 2020</span></div>
    <p class="card-text">At hop3PeakTrail we focus on your career, health, and finances to help you improve your overall well being. Today I’m going to focus on health. The other day I climbed a mountain. During this journey,</p>
    <span class="card-link">LEARN MORE</span>
    <svg class="card-wave" viewBox="0 0 294 90" preserveAspectRatio="none"><path d="M0 50 C60 40 90 80 150 50 C200 25 240 20 294 35 V90 H0Z" fill="var(--yellow-pale)"/><path d="M0 58 C60 48 90 88 150 58 C200 33 240 28 294 43 V90 H0Z" fill="var(--yellow-soft)"/></svg>
  </div>
</article>
<article class="card" style="left:777px;top:1451px">
  <div class="card-photo" role="img" aria-label="Businessman celebrating under falling banknotes" style="background:linear-gradient(160deg,#9a9a96,#6f6f6c 55%,#2e2e2e)"></div>
  <div class="card-title">Vantrel’s Multi-Million</div>
  <div class="card-body">
    <div class="card-meta"><span><i></i>Coach Rae</span><span><b></b>16 December 2020</span></div>
    <p class="card-text">Vantrel’s Project Meridian. A great name for a great project designed to figure out what makes a great team. For this project, Vantrel examined such things as: does the group show similar interests, is it made</p>
    <span class="card-link">LEARN MORE</span>
    <svg class="card-wave" viewBox="0 0 294 90" preserveAspectRatio="none"><path d="M0 50 C60 40 90 80 150 50 C200 25 240 20 294 35 V90 H0Z" fill="var(--yellow-pale)"/><path d="M0 58 C60 48 90 88 150 58 C200 33 240 28 294 43 V90 H0Z" fill="var(--yellow-soft)"/></svg>
  </div>
</article>

<div class="abs pager"><span class="current">1</span><span>2</span><span>3</span><span>…</span><span>6</span></div>

<section class="abs about" role="img" aria-label="Misty mountain ranges at dawn"></section>
<div class="abs about-peak" role="img" aria-label="Person with raised arms standing on a rocky peak"></div>
<h2 class="abs about-title">WHO WE ARE</h2>
<p class="abs about-text">We started hop3PeakTrail with a passion to help people navigate the multitude of decisions in life and develop a process to create stronger wellbeing. We believe that in order to achieve purpose and fulfillment, you need to focus on your health (physical and mental), career, and finances.</p>
<div class="abs btn about-btn">Learn More</div>

<svg class="abs footer-wave" viewBox="0 0 1200 100" preserveAspectRatio="none">
  <path d="M0 22 C150 70 300 80 450 55 C600 30 750 10 900 50 C1020 80 1110 60 1200 30 V100 H0Z" fill="var(--navy)"/>
  <path d="M0 22 C150 70 300 80 450 55 C600 30 750 10 900 50 C1020 80 1110 60 1200 30" fill="none" stroke="#c9a21f" stroke-width="6"/>
</svg>
<footer class="abs footer"></footer>
<div class="abs logo footer-logo">hop3PeakTrail</div>
<span class="abs social" style="left:102px"></span>
<span class="abs social" style="left:145px"></span>
<span class="abs social" style="left:188px"></span>
<span class="abs social" style="left:230px"></span>

<div class="abs footer-col" style="left:371px">
  <h4>Main Menu</h4>
  <a>Blog</a><a>Who We Are</a><a>Our Model</a><a>Who Uses Hop3peaktrail</a><a>Pricing</a>
</div>
<div class="abs footer-col" style="left:596px">
  <h4>Newsletter</h4>
  <p class="news-text">Lorem ipsum dolor sit adipiscing elit, sed do eiusmod</p>
  <div class="news-input">Enter Email</div>
  <div class="btn news-btn">Submit</div>
</div>
<div class="abs footer-col" style="left:884px">
  <h4>Support</h4>
  <a>Contact</a><a>Privacy Policy</a><a>Terms &amp; Conditions</a><a>Cookie Policy</a><a>Media &amp; Promotion Guidelines</a>
</div>
<div class="abs footer-rule"></div>
<p class="abs copyright" style="color:var(--white)">© 2021 hop3peaktrail. All Rights Reserved.</p>

</body>
</html>
```